Create Homepage Header & Search Box for Education Website

This project is relatively small and pays well.
Site: brightmeadowlearning.org
Project Title:
Redesign slider to be a static image/graphic and include a 3 drop down search box.
Project Summary:
We need a new homepage header for brightmeadowlearning.org. The logo, top navigation, and social buttons should remain unchanged. The new header needs to include a static graphic or image and a 3 drop down search box. It can also include some text that speaks to the what our site provides. For text suggestions - see below. Placement for the search box should be to the left under the logo. We will remove the slider functionality and need the design to be static.
Below the current slider images are bar graphs and a pie graph. These can remain as is - or you can make design changes. If you make design changes - please be sure the message doesn't change. Also you can submit one version of the design with this removed if you feel like it helps best accomplish our goal of conversion.
Project Objectives:
The primary objective of the deign is to maximize conversion of clicks to the search box. We need users to gravitate to the search box. Additionally the design should convey trust and academic feel.
Target Market:
High School Graduates and people in their 20s looking for college options.
Potential text:
Tagline Option: "Your #1 Resource for an Affordable Online College Education"
Tagline Option: "Find Affordable Online College Options"
Other Details: Brightmeadow Learning Hub will help you find a more affordable college experience. Look no further to find financial aid information, cost saving tips, and comprehensive college rankings focused on affordability and value.
Or you can also use some placeholder text and I can create the right messaging.
The Search Box:
The search box is pretty standard - you can see examples in the examples below - or in the files I attached. 3 drop downs and a "Search" button.
Examples of some previous designs attached to the project:
These designs are close - but not perfect. These will give you a good general idea for what we need.
Examples of designs at similar websites:
qlvx.org
studyharborweb.net
toplanternschools.com

```html
<!DOCTYPE html>
<html lang="en">
<head>
<meta charset="utf-8">
<title>Brightmeadow Learning Hub – Find Affordable Online College Options</title>
<link href="https://fonts.googleapis.com/css2?family=Bebas+Neue&family=Open+Sans:wght@400;700&family=Ubuntu:wght@400&display=swap" rel="stylesheet">
<style>
  :root {
    --orange: #ef6240;
    --orange-deep: #e4522f;
    --teal: #17938a;
    --teal-dark: #0e5e59;
    --teal-mid: #1a7d76;
    --ink: #1c2126;
    --nav-ink: #262a2e;
    --band: #141b21;
    --slate: #62676d;
    --muted: #7a7a7a;
    --paper: #ffffff;
    --sketch: #f3f3f2;
  }
  * { box-sizing: border-box; margin: 0; padding: 0; }
  html, body { width: 1200px; height: 806px; overflow: hidden; background: var(--paper); }
  body { position: relative; font-family: "Open Sans", Arial, sans-serif; color: var(--ink); }

  .hero-backdrop {
    position: absolute; left: 0; top: 95px; width: 1200px; height: 370px;
    background: radial-gradient(ellipse at 60% 50%, #fafafa 0%, var(--sketch) 70%, #efefee 100%);
  }

  /* Brand */
  .brand {
    position: absolute; left: 85px; top: 3px; width: 124px; height: 124px;
    border-radius: 50%; background: var(--orange);
    border: 5px solid var(--paper); z-index: 3;
    display: flex; align-items: center; justify-content: center; text-align: center;
  }
  .brand-name {
    color: var(--paper); font-family: "Open Sans", Arial, sans-serif; font-weight: 700;
    font-size: 15px; line-height: 1.15; width: 90px;
  }

  /* Navigation */
  .main-nav { position: absolute; top: 31px; left: 0; height: 30px; }
  .main-nav a {
    position: absolute; top: 0; white-space: nowrap;
    font-family: "Ubuntu", Arial, sans-serif; font-size: 20px; color: var(--nav-ink); text-decoration: none;
  }
  .main-nav a.is-current { color: var(--orange); border-bottom: 2px solid var(--orange); padding-bottom: 1px; }

  .social { position: absolute; top: 33px; left: 1092px; display: flex; gap: 15px; }
  .social span { width: 27px; height: 27px; border-radius: 4px; display: block; }
  .social .s1 { background: #3b5998; }
  .social .s2 { background: #1da1f2; }
  .social .s3 { background: #dc3b2e; }

  /* Search panel */
  .search-panel {
    position: absolute; left: 94px; top: 113px; width: 294px; height: 331px;
    background: var(--teal); z-index: 2;
  }
  .search-title { position: absolute; right: 24px; top: 8px; text-align: right; font-family: "Bebas Neue", Impact, sans-serif; }
  .search-title .lead { display: block; color: var(--paper); font-size: 32px; line-height: 32px; }
  .search-title .big { display: block; color: var(--ink); font-size: 50px; line-height: 46px; letter-spacing: 0.5px; text-shadow: -2px 2px 0 var(--paper); }

  .search-step { position: absolute; left: 16px; width: 254px; height: 46px; background: var(--teal-mid); }
  .step-num {
    position: absolute; left: 0; top: -2px; width: 50px; height: 50px; border-radius: 50%;
    background: var(--teal-dark); color: var(--paper);
    font-family: "Bebas Neue", Impact, sans-serif; font-size: 40px; line-height: 54px; text-align: center;
  }
  .step-select {
    position: absolute; left: 52px; top: 3px; width: 196px; height: 40px; background: var(--paper);
    font-size: 14px; line-height: 40px; padding-left: 12px; color: #333;
  }
  .step-select svg { position: absolute; right: 8px; top: 12px; }
  .search-step:nth-of-type(2) .step-select,
  .search-step:nth-of-type(3) .step-select { background: #dbeeed; }

  .find-button {
    position: absolute; left: 27px; top: 269px; width: 246px; height: 48px;
    background: var(--orange-deep); border: 3px solid var(--paper);
    color: var(--paper); font-family: "Bebas Neue", Impact, sans-serif; font-size: 32px; line-height: 44px; text-align: center;
  }

  .pointer-arrow { position: absolute; left: 425px; top: 128px; }

  .headline { position: absolute; left: 562px; top: 126px; font-family: "Bebas Neue", Impact, sans-serif; color: var(--ink); font-weight: 400; }
  .headline .h-small { display: block; font-size: 50px; line-height: 48px; }
  .headline .h-large { display: block; font-size: 66px; line-height: 60px; letter-spacing: 0.3px; }

  .intro-box {
    position: absolute; left: 551px; top: 303px; width: 442px; height: 134px; background: var(--slate);
    color: var(--paper); padding: 16px 25px 0 20px; font-size: 16.5px; line-height: 25px; text-align: justify;
  }
  .intro-box strong { font-weight: 700; }

  /* Stats band */
  .stats-band { position: absolute; left: 0; top: 484px; width: 1200px; height: 142px; background: var(--band); }
  .debt-bar { position: absolute; left: 94px; width: 194px; height: 44px; border: 1px solid #2a333b; }
  .debt-bar .fill { position: absolute; left: 0; top: 0; bottom: 0; background: var(--teal); }
  .debt-bar .amount { position: absolute; left: 24px; top: 0; font-family: "Bebas Neue", Impact, sans-serif; font-size: 32px; line-height: 46px; color: var(--paper); }
  .stat-label { position: absolute; font-family: "Bebas Neue", Impact, sans-serif; font-size: 24px; line-height: 25px; color: var(--orange); }
  .loan-pie { position: absolute; left: 548px; top: 14px; }
  .pie-value { position: absolute; left: 548px; top: 48px; width: 100px; text-align: center; font-family: "Bebas Neue", Impact, sans-serif; font-size: 32px; color: var(--paper); }
  .band-note { position: absolute; left: 846px; top: 16px; width: 420px; }
  .band-note h2 { font-weight: 400; font-size: 18.5px; color: var(--orange); white-space: nowrap; }
  .band-note p { margin-top: 8px; margin-left: -12px; width: 420px; text-align: center; color: var(--paper); font-size: 16px; line-height: 24px; }

  /* Feature cards */
  .feature { position: absolute; top: 670px; width: 340px; }
  .feature-icon { position: absolute; left: 0; top: 5px; width: 90px; height: 90px; border-radius: 50%; background: var(--orange); display: flex; align-items: center; justify-content: center; }
  .feature h3 { position: absolute; left: 106px; top: 0; width: 250px; font-weight: 400; font-size: 18.5px; line-height: 24px; color: #333; }
  .feature p { position: absolute; left: 106px; width: 240px; font-size: 14px; line-height: 24px; color: var(--muted); }
  .read-more {
    position: absolute; height: 26px; padding: 0 10px; border: 1px solid #ddd; border-radius: 3px; background: #fff;
    font-size: 13px; line-height: 24px; color: #c0392b; white-space: nowrap;
  }
</style>
</head>
<body>

<div class="hero-backdrop" role="img" aria-label="Faint hand-sketched maths formulas, graphs and diagrams on white paper"></div>

<div class="brand"><span class="brand-name">Brightmeadow Learning Hub</span></div>

<nav class="main-nav">
  <a href="#" style="left:272px">Home</a>
  <a href="#" class="is-current" style="left:373px">Financial Aid</a>
  <a href="#" style="left:538px">Cost Savings</a>
  <a href="#" style="left:708px">Colleges</a>
  <a href="#" style="left:835px">Awards</a>
  <a href="#" style="left:953px">Blog</a>
</nav>

<div class="social" aria-label="Social links"><span class="s1"></span><span class="s2"></span><span class="s3"></span></div>

<section class="search-panel">
  <h2 class="search-title"><span class="lead">Start your</span><span class="big">Search now!</span></h2>
  <div class="search-step" style="top:94px"><span class="step-num">1</span><div class="step-select">Select a Degree Level
    <svg width="18" height="16" viewBox="0 0 18 16" fill="#ef6240"><g><circle cx="3" cy="2" r="1.3"/><circle cx="8" cy="2" r="1.3"/><circle cx="13" cy="2" r="1.3"/><circle cx="3" cy="7" r="1.3"/><circle cx="8" cy="7" r="1.3"/><circle cx="13" cy="7" r="1.3"/><circle cx="8" cy="12" r="1.3"/><circle cx="4" cy="10" r="1.1"/><circle cx="12" cy="10" r="1.1"/></g></svg></div></div>
  <div class="search-step" style="top:149px"><span class="step-num">2</span><div class="step-select">Select a Category
    <svg width="18" height="16" viewBox="0 0 18 16" fill="#ef6240"><g><circle cx="3" cy="2" r="1.3"/><circle cx="8" cy="2" r="1.3"/><circle cx="13" cy="2" r="1.3"/><circle cx="3" cy="7" r="1.3"/><circle cx="8" cy="7" r="1.3"/><circle cx="13" cy="7" r="1.3"/><circle cx="8" cy="12" r="1.3"/><circle cx="4" cy="10" r="1.1"/><circle cx="12" cy="10" r="1.1"/></g></svg></div></div>
  <div class="search-step" style="top:204px"><span class="step-num">3</span><div class="step-select">Select a Subject
    <svg width="18" height="16" viewBox="0 0 18 16" fill="#ef6240"><g><circle cx="3" cy="2" r="1.3"/><circle cx="8" cy="2" r="1.3"/><circle cx="13" cy="2" r="1.3"/><circle cx="3" cy="7" r="1.3"/><circle cx="8" cy="7" r="1.3"/><circle cx="13" cy="7" r="1.3"/><circle cx="8" cy="12" r="1.3"/><circle cx="4" cy="10" r="1.1"/><circle cx="12" cy="10" r="1.1"/></g></svg></div></div>
  <div class="find-button">Find Colleges!</div>
</section>

<svg class="pointer-arrow" width="118" height="100" viewBox="0 0 118 100" aria-hidden="true">
  <g fill="none" stroke="#ef6240" stroke-width="7" stroke-linecap="round" stroke-linejoin="round" opacity="0.9">
    <path d="M112 42 L14 44"/>
    <path d="M52 6 L12 44 L44 92"/>
  </g>
</svg>

<h1 class="headline">
  <span class="h-small">Find</span>
  <span class="h-large">Affordable Online</span>
  <span class="h-large">College Options</span>
</h1>

<div class="intro-box"><strong>Find a more affordable college experience.</strong> Look no further to find financial aid information, cost saving tips, and comprehensive college rankings focused on affordability and value.</div>

<section class="stats-band">
  <div class="debt-bar" style="top:17px"><span class="fill" style="width:109px"></span><span class="amount">$12,500</span></div>
  <div class="debt-bar" style="top:74px"><span class="fill" style="width:161px"></span><span class="amount">$26,600</span></div>
  <div class="stat-label" style="left:314px;top:26px">Avg student debt in 1996</div>
  <div class="stat-label" style="left:314px;top:83px">Avg student debt in 2011</div>
  <svg class="loan-pie" width="100" height="100" viewBox="0 0 100 100" aria-hidden="true">
    <circle cx="50" cy="50" r="48" fill="#0f1519" stroke="#2a333b" stroke-width="1"/>
    <path d="M50 50 L50 2 A48 48 0 1 0 92.5 72.3 Z" fill="#17938a"/>
    <circle cx="50" cy="50" r="34" fill="#141b21"/>
  </svg>
  <div class="pie-value">66%</div>
  <div class="stat-label" style="left:664px;top:46px">Pct of students<br>with loans</div>
  <div class="band-note">
    <h2>College Costs Rising &amp; Student Debt Ballooning</h2>
    <p>Brightmeadow Learning Hub helps students find affordable college options and provides information about financial aid and college rankings.</p>
  </div>
</section>

<article class="feature" style="left:89px">
  <div class="feature-icon"><svg width="40" height="60" viewBox="0 0 40 60" aria-hidden="true"><text x="20" y="50" text-anchor="middle" font-family="Open Sans, Arial, sans-serif" font-weight="700" font-size="56" fill="#fff">$</text></svg></div>
  <h3>Financial Aid</h3>
  <p style="top:42px">The nuts of bolts of financial aid – what's available and how to apply.</p>
  <span class="read-more" style="left:259px;top:99px">Read more</span>
</article>

<article class="feature" style="left:467px">
  <div class="feature-icon"><svg width="60" height="48" viewBox="0 0 60 48" aria-hidden="true"><g fill="#fff"><rect x="4" y="30" width="9" height="16"/><rect x="18" y="24" width="9" height="22"/><rect x="32" y="16" width="9" height="30"/><rect x="46" y="8" width="9" height="38"/></g><path d="M3 24 L18 14 L30 18 L52 2" fill="none" stroke="#fff" stroke-width="3"/><path d="M45 1 L54 1 L53 10" fill="none" stroke="#fff" stroke-width="3"/></svg></div>
  <h3>Rising College Costs: Who is Helping?</h3>
  <p style="top:66px">Who's helping and what does that mean for you?</p>
  <span class="read-more" style="left:259px;top:123px">Read more</span>
</article>

<article class="feature" style="left:845px">
  <div class="feature-icon"><svg width="60" height="48" viewBox="0 0 60 48" aria-hidden="true"><ellipse cx="30" cy="24" rx="24" ry="19" fill="#fff"/><rect x="14" y="36" width="7" height="10" fill="#fff"/><rect x="38" y="36" width="7" height="10" fill="#fff"/><text x="30" y="32" text-anchor="middle" font-family="Open Sans, Arial, sans-serif" font-weight="700" font-size="22" fill="#ef6240">$</text></svg></div>
  <h3>Affordability Tips</h3>
  <p style="top:42px">Check out our tips for how you can make college more affordable</p>
  <span class="read-more" style="left:260px;top:99px">Read more</span>
</article>

</body>
</html>
```